Men's Ministry Vesperine Church "Note to Clergy"

We need to update brochure line-up to the 21st Century. This piece will explain the value that a men's ministry affords a local parish. A majority of priests (male and female) do not know what the Kinsmen of St. Orwin can do to help them lay a solid foundation to grow, become more diversified, and present a positive picture for the local community
Updates

Under Must Not or avoid, please do not put the Kinsmen logo on the Front Panel, back shield reduce keep low key it. We need a 21st Century look that will appeal to Millennials, Gen-Xers, younger generation. Shield was created in 1883, it is about time we changed it.

Target Market(s)

Male and female clergy in the Hallowmere Vesperine Church

Industry/Entity Type

Non-Profit

Font styles to use
Serif

Requirements
Must have
• Slogan "Unleash the Orwin Within"
• Snappy enough to invite people to pick -up
Nice to have
• Want to keep Kinsmen of St. Orwin Logo on back panel, low keyed with address, web page and phone
Should not have
• political issues or political correctness

```html
<!DOCTYPE html>
<html lang="en">
<head>
<meta charset="utf-8">
<title>Kinsmen of St. Orwin – Note to Clergy Brochure</title>
<link rel="stylesheet" href="https://fonts.googleapis.com/css2?family=Crimson+Pro:wght@400;600;700&family=Oswald:wght@500&display=swap">
<style>
  :root {
    --red: #c3192f;
    --blue: #0d3c96;
    --blue-deep: #071f66;
    --ink: #1c1c1c;
    --paper: #ffffff;
    --stage: #e6e6e6;
    --sunset-top: #d9b48a;
    --sunset-bottom: #3d2418;
    --sky: #5d93cf;
    --glow: #f1d77a;
    --grass: #6f9a2a;
  }
  * { box-sizing: border-box; margin: 0; padding: 0; }
  html, body { width: 1027px; height: 1200px; overflow: hidden; }
  body { background: var(--stage); font-family: "Crimson Pro", Georgia, serif; color: var(--ink); position: relative; }

  .brochure {
    position: absolute; left: 48px; top: 240px;
    width: 930px; height: 720px;
    background: var(--paper);
    box-shadow: 0 10px 30px rgba(0,0,0,.25);
    overflow: hidden;
  }
  .panel { position: absolute; top: 0; width: 310px; height: 720px; }
  .panel--inside { left: 0; }
  .panel--back { left: 310px; }
  .panel--front { left: 620px; }

  .fold { position: absolute; top: 0; width: 24px; height: 720px; z-index: 5; pointer-events: none; }
  .fold--one { left: 310px; background: linear-gradient(90deg, rgba(0,0,0,.12), rgba(0,0,0,0)); }
  .fold--two { left: 596px; background: linear-gradient(90deg, rgba(0,0,0,0), rgba(0,0,0,.1)); }

  .photo { position: absolute; }
  .photo--gathering {
    left: 0; top: 390px; width: 310px; height: 220px;
    background: linear-gradient(180deg, #ffffff 0%, var(--sunset-top) 35%, #8a5a38 70%, var(--sunset-bottom) 100%);
  }
  .photo--field {
    left: 620px; top: 0; width: 310px; height: 480px;
    background: linear-gradient(180deg, var(--sky) 0%, #8fb4d8 38%, var(--glow) 55%, var(--grass) 70%, #4d7a1c 100%);
  }

  .wave { position: absolute; left: 0; top: 0; width: 930px; height: 720px; z-index: 2; }

  .ministry { position: absolute; left: 26px; top: 30px; width: 262px; z-index: 3; }
  .ministry__title { color: var(--red); font-weight: 700; font-size: 19px; line-height: 1.15; margin-bottom: 14px; }
  .ministry__list { list-style: none; font-size: 12.5px; line-height: 1.3; }
  .ministry__list li { position: relative; padding-left: 14px; margin-bottom: 9px; text-align: justify; }
  .ministry__list li::before {
    content: ""; position: absolute; left: 0; top: 6px;
    width: 5px; height: 5px; border-radius: 50%; background: var(--red);
  }

  .contact { position: absolute; left: 310px; top: 0; width: 310px; text-align: center; z-index: 3; }
  .contact__name { margin-top: 120px; font-size: 17px; color: #333; letter-spacing: .3px; }
  .contact__mark { display: inline-block; width: 10px; height: 10px; border-radius: 50%; background: var(--red); margin-right: 6px; vertical-align: middle; }
  .contact__item { margin-top: 34px; font-size: 13px; font-weight: 600; line-height: 1.25; }
  .contact__item--tight { margin-top: 22px; }
  .contact__icon { display: block; margin: 0 auto 8px; width: 22px; height: 22px; }

  .map {
    position: absolute; left: 352px; top: 440px; width: 142px; height: 142px;
    border-radius: 50%; border: 6px solid var(--red); z-index: 4;
    background: linear-gradient(135deg, #f2f2f2 0%, #e4e4e4 60%, #cfe3c4 100%);
  }

  .slogan { position: absolute; left: 620px; top: 500px; width: 310px; text-align: center; color: var(--paper); z-index: 3; }
  .slogan__lead { font-size: 40px; line-height: 1; letter-spacing: 1px; }
  .slogan__main { font-family: "Oswald", "Arial Narrow", sans-serif; font-weight: 500; font-size: 46px; line-height: 1.05; }

  .web-pill {
    position: absolute; top: 648px; width: 236px; height: 36px;
    border-radius: 18px; background: var(--red); color: var(--paper);
    font-weight: 700; font-size: 17px; line-height: 36px; text-align: center; z-index: 3;
    box-shadow: 0 2px 4px rgba(0,0,0,.25);
  }
  .web-pill--inside { left: 37px; }
  .web-pill--back { left: 347px; }
  .web-pill--front { left: 657px; }
</style>
</head>
<body>
  <main class="brochure">
    <div class="photo photo--gathering" role="img" aria-label="Silhouetted family raising hands before a cross at sunset"></div>
    <div class="photo photo--field" role="img" aria-label="Man with arms raised in a green field under a sunrise sky"></div>

    <svg class="wave" viewBox="0 0 930 720" aria-hidden="true">
      <defs>
        <linearGradient id="blueBand" x1="0" y1="0" x2="0" y2="1">
          <stop offset="0" stop-color="var(--blue)"/>
          <stop offset="1" stop-color="var(--blue-deep)"/>
        </linearGradient>
      </defs>
      <path d="M0 572 C150 632 300 560 450 474 S750 380 930 392 L930 720 L0 720Z" fill="var(--red)"/>
      <path d="M0 584 C150 644 300 572 450 486 S750 392 930 404 L930 720 L0 720Z" fill="#ffffff"/>
      <path d="M0 590 C150 650 300 578 450 492 S750 398 930 410 L930 720 L0 720Z" fill="url(#blueBand)"/>
    </svg>

    <section class="panel panel--inside">
      <div class="ministry">
        <h2 class="ministry__title">The Kinsmen of St. Orwin<br>Community of Ministry for Men</h2>
        <ul class="ministry__list">
          <li>Building Partnerships and Alliances to gain resources plus state of the art facilitating, mentoring, and/or leadership training for expanding Congregational Vitality.</li>
          <li>Providing Web Page, Friendlink, Blog, Worknet, and Clipstream capabilities for idea sharing, inquiries, and testimonials</li>
          <li>Special event planning for local parish, deanery, or parish use during a ministry fair day atmosphere Assisting Parishes and Dioceses in creating Men’s Ministry links and formats to disciple men to Christ</li>
          <li>Primary resource and clearing house for Restorative Justice Ministry program opportunities including: Threshold, Veteran’s Courts, Half-Way Houses, in Prison Kinsmen ministry, Step-Houses, and Summer Camps for the children of incarcerated men.</li>
          <li>Facilitating local parishes develop Veteran Friendly Congregations to provide a safe haven for veterans encountering post dramatic stress disorder, addictions, suicidal tendencies, spouse abuse, and divorces</li>
        </ul>
      </div>
    </section>

    <section class="contact">
      <p class="contact__name"><span class="contact__mark"></span>Kinsmen of St. Orwin</p>
      <div class="contact__item">
        <svg class="contact__icon" viewBox="0 0 24 24" aria-hidden="true"><circle cx="12" cy="12" r="10.5" fill="none" stroke="var(--red)" stroke-width="1.4"/><path d="M12 18s-4-4.2-4-7a4 4 0 0 1 8 0c0 2.8-4 7-4 7z" fill="none" stroke="var(--red)" stroke-width="1.4"/><circle cx="12" cy="11" r="1.3" fill="var(--red)"/></svg>
        P.O. Box 418<br>Larkford, PA 15990
      </div>
      <div class="contact__item contact__item--tight">
        <svg class="contact__icon" viewBox="0 0 24 24" aria-hidden="true"><circle cx="12" cy="12" r="10.5" fill="none" stroke="var(--red)" stroke-width="1.4"/><path d="M8.5 7.5l2 2-1.2 1.4a7 7 0 0 0 3.8 3.8l1.4-1.2 2 2-1.5 1.5c-3.8 0-8-4.2-8-8z" fill="none" stroke="var(--red)" stroke-width="1.4" stroke-linejoin="round"/></svg>
        (555) 014-2271
      </div>
      <div class="contact__item contact__item--tight">
        <svg class="contact__icon" viewBox="0 0 24 24" aria-hidden="true"><circle cx="12" cy="12" r="10.5" fill="none" stroke="var(--red)" stroke-width="1.4"/><rect x="7" y="8.5" width="10" height="7" fill="none" stroke="var(--red)" stroke-width="1.4"/><path d="M7 8.5l5 4 5-4" fill="none" stroke="var(--red)" stroke-width="1.4"/></svg>
        kinsmenofstorwin@kinsmenorwin.net
      </div>
    </section>

    <div class="map" role="img" aria-label="Street map showing the ministry office location"></div>

    <div class="slogan">
      <p class="slogan__lead">UNLEASH THE</p>
      <p class="slogan__main">ORWIN WITHIN</p>
    </div>

    <p class="web-pill web-pill--inside">www.kinsmenorwin.net</p>
    <p class="web-pill web-pill--back">www.kinsmenorwin.net</p>
    <p class="web-pill web-pill--front">www.kinsmenorwin.net</p>

    <div class="fold fold--one"></div>
    <div class="fold fold--two"></div>
  </main>
</body>
</html>
```